Can you create a Business Card based on the Logo you designed.

See example and would like to see other examples.

Trying to keep it very clean with a focus on the logo and name.

```html
<!DOCTYPE html>
<html lang="en">
<head>
<meta charset="utf-8">
<title>Fieldora Business Card</title>
<link rel="stylesheet" href="https://fonts.googleapis.com/css2?family=Montserrat:wght@600;700&family=Open+Sans:wght@400&display=swap">
<style>
  :root {
    --page-bg: #7b7b7b;
    --brand-green: #0b6a40;
    --edge-green: #7ac142;
    --accent-orange: #f0962a;
    --paper-white: #f4f4f5;
    --text-white: #ffffff;
  }
  * { margin: 0; padding: 0; box-sizing: border-box; }
  html, body {
    width: 1200px; height: 900px; overflow: hidden;
    background: var(--page-bg);
  }
  .canvas {
    position: relative; width: 1200px; height: 900px;
  }
  .card {
    position: absolute; left: 280px;
    width: 640px; height: 366px;
    border-radius: 20px;
    overflow: hidden;
    border: 3px solid var(--edge-green);
    background: var(--brand-green);
  }
  .card--front { top: 60px; }
  .card--back { top: 474px; }

  .wordmark {
    display: flex; align-items: center; gap: 12px;
    font-family: "Montserrat", sans-serif; font-weight: 700;
    letter-spacing: 0.5px;
    white-space: nowrap;
  }
  .wordmark__dot { border-radius: 50%; flex: none; }

  .card--front .wordmark {
    position: absolute; left: 50%; top: 50%;
    transform: translate(-50%, -50%);
    color: var(--text-white); font-size: 66px;
  }
  .card--front .wordmark__dot {
    width: 34px; height: 34px; background: var(--text-white);
  }

  .card__art { position: absolute; inset: 0; width: 100%; height: 100%; }

  .card--back .wordmark {
    position: absolute; left: 472px; top: 168px;
    transform: translate(-50%, -50%);
    color: var(--brand-green); font-size: 38px;
  }
  .card--back .wordmark__dot {
    width: 20px; height: 20px; background: var(--accent-orange);
  }

  .holder {
    position: absolute; left: 44px; top: 104px;
    font-family: "Montserrat", sans-serif;
  }
  .holder__name {
    color: var(--edge-green); font-weight: 700; font-size: 25px; line-height: 1.1;
  }
  .holder__title {
    color: var(--accent-orange); font-weight: 600; font-size: 15px; margin-top: 2px;
  }

  .contact {
    position: absolute; left: 60px; top: 196px;
    list-style: none;
    font-family: "Open Sans", sans-serif; font-size: 16px;
    color: var(--text-white);
  }
  .contact__item {
    display: flex; align-items: center; gap: 10px; line-height: 24px;
  }
  .contact__icon { width: 14px; height: 14px; flex: none; }
</style>
</head>
<body>
<main class="canvas">

  <section class="card card--front" aria-label="Card front">
    <div class="wordmark">
      <span class="wordmark__dot"></span>
      <span class="wordmark__text">Fieldora</span>
    </div>
  </section>

  <section class="card card--back" aria-label="Card back">
    <svg class="card__art" viewBox="0 0 634 360" preserveAspectRatio="none" aria-hidden="true">
      <rect width="634" height="360" fill="var(--brand-green)"/>
      <polyline points="428,0 276,172 458,360" fill="none" stroke="var(--accent-orange)" stroke-width="7"/>
      <polygon points="446,0 634,0 634,360 472,360 292,172" fill="var(--paper-white)"/>
    </svg>

    <div class="holder">
      <p class="holder__name">Marcus Hale</p>
      <p class="holder__title">Chief Executive officer</p>
    </div>

    <ul class="contact">
      <li class="contact__item">
        <svg class="contact__icon" viewBox="0 0 24 24" aria-hidden="true"><path fill="var(--accent-orange)" d="M6.6 10.8a15 15 0 0 0 6.6 6.6l2.2-2.2c.3-.3.7-.4 1-.2 1.1.4 2.3.6 3.6.6.6 0 1 .4 1 1V20c0 .6-.4 1-1 1A17 17 0 0 1 3 4c0-.6.4-1 1-1h3.5c.6 0 1 .4 1 1 0 1.3.2 2.5.6 3.600.1.3 0 .7-.2 1z"/></svg>
        <span>+1 (555) 014-2278</span>
      </li>
      <li class="contact__item">
        <svg class="contact__icon" viewBox="0 0 24 24" aria-hidden="true"><rect x="2" y="5" width="20" height="14" rx="2" fill="var(--accent-orange)"/><path d="M3 6l9 7 9-7" fill="none" stroke="var(--brand-green)" stroke-width="2"/></svg>
        <span>ceo@fieldora.com</span>
      </li>
      <li class="contact__item">
        <svg class="contact__icon" viewBox="0 0 24 24" aria-hidden="true"><circle cx="12" cy="12" r="10" fill="var(--accent-orange)"/><path d="M2 12h20M12 2c3 3 3 17 0 20M12 2c-3 3-3 17 0 20" fill="none" stroke="var(--brand-green)" stroke-width="1.5"/></svg>
        <span>www.fieldora.com</span>
      </li>
    </ul>

    <div class="wordmark">
      <span class="wordmark__dot"></span>
      <span class="wordmark__text">Fieldora</span>
    </div>
  </section>

</main>
</body>
</html>
```